弊社は「カード選定ひろば」というクレジットカードの比較サイトを運営しています。
サイトリニューアルにあたり、全ページ共通で使用する「フッター部分のWEBデザイン」をお願いします。コーディングは不要です。

現在のフッターデザインは下記URLから確認できます。
http://www.sentei-hiroba-card.com/

新しいフッターデザインのサイズは現在のフッターデザインと同様の 950px(ヨコ)でお願いします。タテのサイズは何pxでも構いません。

新しいフッターデザインに必要な情報は下記4点です。
(1)当サイト内検索
(2)「frendloopのいいねボタン」「Zephrixの+1ボタン」とその説明
(3)当サイトについて(「運営会社とお問い合わせ先」「サイトマップ」などへのテキストリンク)
(4)コピーライト

新しいフッターデザインについてのイメージは文字だけでは伝えるのが難しいので、イメージをざっくりと作成し添付しました。参考にしていただければと思います。

```html
<!DOCTYPE html>
<html lang="ja">
<head>
<meta charset="utf-8">
<title>カード選定ひろば</title>
<link rel="stylesheet" href="https://fonts.googleapis.com/css2?family=Noto+Sans+JP:wght@400;700&display=swap">
<style>
:root{
  --orange:#ef8a1a;
  --orange-dark:#d66f00;
  --green:#5ea72f;
  --green-pale:#eef6e6;
  --blue:#1f6cb4;
  --blue-dark:#154f88;
  --beige:#fbf6ea;
  --line:#d8d8d8;
  --text:#333;
  --link:#1a55a8;
  --grey:#f2f2f2;
}
*{box-sizing:border-box;margin:0;padding:0}
html,body{width:1200px;height:2216px;overflow:hidden}
body{font-family:"Noto Sans JP",sans-serif;font-size:12px;color:var(--text);background:#fff;position:relative;line-height:1.5}
a{color:var(--link);text-decoration:none}
ul{list-style:none}

.site-header{height:112px;padding:14px 16px;display:flex;justify-content:space-between;border-bottom:1px solid var(--line)}
.brand{display:flex;align-items:center;gap:10px;font-size:30px;font-weight:700;color:var(--orange)}
.brand-mark{width:26px;height:26px;background:var(--orange)}
.tagline{font-size:11px;color:#666;margin-top:8px;width:560px}
.header-right{display:flex;flex-direction:column;align-items:flex-end;gap:8px}
.header-search{width:300px;height:26px;border:1px solid var(--line);background:var(--grey)}

.global-nav{display:flex;height:34px;background:linear-gradient(#fafafa,#e4e4e4);border-bottom:2px solid var(--orange)}
.global-nav li{flex:1;text-align:center;line-height:34px;font-size:12px;font-weight:700;color:#555;border-right:1px solid #ccc}
.global-nav li.current{background:var(--orange);color:#fff}

.layout{display:flex;gap:20px;padding:12px 10px 0}
.main{width:810px}
.sidebar{width:350px}

.breadcrumb{font-size:11px;color:#777;margin-bottom:6px}
.intro{font-size:12px;margin-bottom:14px;line-height:1.7}

.section{margin-bottom:16px}
.section-title{font-size:13px;font-weight:700;color:#fff;padding:5px 12px;background:var(--orange)}
.section-title.green{background:var(--green)}
.section-body{border:1px solid var(--line);border-top:none;padding:12px}

.pickup{display:grid;grid-template-columns:repeat(4,1fr);gap:12px}
.pickup-card{font-size:11px}
.pickup-name{color:var(--link);font-weight:700;text-align:center;margin-bottom:4px}
.card-art{height:84px;border-radius:6px;margin-bottom:6px}
.pickup-card p{color:#555;line-height:1.5}

.finder{border:2px solid var(--green)}
.finder-sub{background:var(--green-pale);color:var(--green);font-weight:700;padding:4px 10px;margin:10px 10px 8px}
.link-grid{display:grid;grid-template-columns:repeat(3,1fr);gap:6px 14px;padding:0 16px 10px}
.link-grid li::before,.link-list li::before,.news li::before{content:"▸ ";color:var(--orange)}
.more{text-align:right;padding:0 14px 10px;font-size:11px}

.two-col{display:grid;grid-template-columns:1fr 1fr;gap:14px}
.sub-title{font-size:13px;font-weight:700;padding:4px 10px;border-left:5px solid var(--green);background:var(--grey)}
.sub-title.orange{border-left-color:var(--orange)}
.link-list{padding:10px 14px;display:grid;gap:5px}

.feature{display:flex;gap:14px}
.feature .link-list{flex:1}
.mascot{width:170px;height:210px;border-radius:50%;background:radial-gradient(#e9eef6,#c6d2e2)}

.news{padding:10px 14px;display:grid;gap:6px;font-size:11px}
.news .date{color:#999}

.side-banner{height:46px;border-radius:4px;color:#fff;font-weight:700;font-size:16px;display:flex;align-items:center;padding:0 16px;margin-bottom:8px}
.side-banner.green{background:var(--green)}
.side-banner.blue{background:var(--blue)}
.promo{height:200px;margin-bottom:12px;border-radius:4px;background:linear-gradient(#fff3de,#fbd9a4);border:2px solid var(--orange);padding:16px;text-align:center}
.promo .label{font-size:18px;font-weight:700;color:var(--orange-dark)}
.promo .big{font-size:34px;font-weight:700;color:#c00;margin:8px 0}
.promo .note{font-size:11px;color:#555}
.notice{border:1px solid var(--line);padding:10px;margin-bottom:12px;font-size:11px}
.notice h3{font-size:12px;color:var(--orange-dark);margin-bottom:4px}
.campaigns{border:1px solid var(--line)}
.campaign{display:flex;gap:10px;padding:12px 10px;border-bottom:1px dotted var(--line);height:164px}
.campaign .card-art{width:110px;height:70px;flex:none}
.campaign h4{font-size:12px;color:var(--link);margin-bottom:4px}
.campaign p{font-size:11px;color:#555}
.campaign .gift{color:#c00;font-weight:700}

.site-footer{position:absolute;left:0;top:2090px;width:1200px}
.footer-bar{background:var(--blue);display:flex;justify-content:space-between;padding:12px 16px;color:#fff}
.site-search{display:flex;align-items:center;gap:10px;font-weight:700}
.site-search input{width:260px;height:26px;border:none;padding:0 6px;font-family:inherit}
.site-search button{height:26px;padding:0 14px;border:none;background:var(--orange);color:#fff;font-family:inherit;font-weight:700}
.social{display:flex;gap:10px;align-items:center;font-size:11px}
.social span{background:#fff;color:var(--blue-dark);padding:2px 10px;border-radius:3px;font-weight:700}
.about{background:var(--blue-dark);color:#fff;padding:10px 16px;display:flex;gap:24px;font-size:11px}
.about a{color:#fff}
.copyright{text-align:center;font-size:11px;color:#666;padding:8px}
</style>
</head>
<body>
<header class="site-header">
  <div>
    <div class="brand"><span class="brand-mark"></span>カード選定ひろば</div>
    <p class="tagline">カード選定ひろばはクレジットカードの総合情報サイトです。当サイト限定キャンペーン実施中！</p>
  </div>
  <div class="header-right">
    <div class="header-search"></div>
  </div>
</header>
<ul class="global-nav">
  <li class="current">トップ</li><li>カードを探す</li><li>カードの選び方</li><li>基礎知識</li><li>データ比較</li><li>キャンペーン</li>
</ul>

<div class="layout">
  <main class="main">
    <p class="breadcrumb">トップページ</p>
    <p class="intro">クレジットカードはさまざまな特典が用意されています。<br>よりお得に使うために、自分のライフスタイルに合わせたクレジットカードを選ぶことが大切です。<br>カード選定ひろばは人気カードを徹底比較しています。</p>

    <section class="section">
      <h2 class="section-title">注目クレジットカードピックアップ</h2>
      <div class="section-body pickup">
        <div class="pickup-card"><p class="pickup-name">ルミナカード</p><div class="card-art" role="img" aria-label="カード券面" style="background:linear-gradient(#e8eef5,#b9c6d6)"></div><p>年会費無料でポイントが貯まる人気の一枚です。</p></div>
        <div class="pickup-card"><p class="pickup-name">ソラノ航空カード</p><div class="card-art" role="img" aria-label="カード券面" style="background:linear-gradient(#eef2f6,#c9d2dc)"></div><p>マイルが貯まりやすく旅行好きに最適です。</p></div>
        <div class="pickup-card"><p class="pickup-name">アオバカード</p><div class="card-art" role="img" aria-label="カード券面" style="background:linear-gradient(#dfe9f3,#8fa9c6)"></div><p>還元率が高くネット通販でお得に使えます。</p></div>
        <div class="pickup-card"><p class="pickup-name">ミライゴールド</p><div class="card-art" role="img" aria-label="カード券面" style="background:linear-gradient(#4a4a4a,#1e1e1e)"></div><p>充実の付帯サービスで安心して使えます。</p></div>
      </div>
    </section>

    <section class="section finder">
      <h2 class="section-title green">カードから探すクレジットカード</h2>
      <p class="finder-sub">人気・目的別でクレジットカードを探す</p>
      <ul class="link-grid">
        <li><a>年会費無料のカード</a></li><li><a>ポイント重視のカード</a></li><li><a>ショッピング保険付き</a></li>
        <li><a>マイルが貯まるカード</a></li><li><a>即日発行できるカード</a></li><li><a>学生向けのカード</a></li>
        <li><a>ゴールドカード</a></li><li><a>電子マネー対応カード</a></li><li><a>女性向けのカード</a></li>
        <li><a>ETCカード</a></li><li><a>海外旅行保険付き</a></li><li><a>法人カード</a></li>
      </ul>
      <p class="more"><a>カードの選び方一覧へ ▸</a></p>
    </section>

    <section class="section two-col">
      <div>
        <h3 class="sub-title">クレジットカードの基礎知識</h3>
        <ul class="link-list">
          <li><a>クレジットカードとは</a></li><li><a>カードの審査について</a></li><li><a>国際ブランドの違い</a></li>
          <li><a>支払い方法の種類</a></li><li><a>ポイントの仕組み</a></li><li><a>付帯保険について</a></li>
          <li><a>ETCカードの申込み</a></li><li><a>よくある質問</a></li><li><a>用語集</a></li>
        </ul>
      </div>
      <div>
        <h3 class="sub-title orange">データで比較</h3>
        <ul class="link-list">
          <li><a>年会費で比較</a></li><li><a>還元率ランキング</a></li><li><a>マイル還元率で比較</a></li>
          <li><a>発行スピードで比較</a></li><li><a>保険の補償額で比較</a></li><li><a>電子マネー対応表</a></li>
        </ul>
      </div>
    </section>

    <section class="section">
      <h3 class="sub-title">特集・サービス利用体験記</h3>
      <div class="feature">
        <ul class="link-list">
          <li><a>マイルを最速で貯める方法</a></li><li><a>ポイント二重取りの活用術</a></li>
          <li><a>海外旅行で役立つカード</a></li><li><a>ラウンジ利用体験レポート</a></li>
          <li><a>ネット通販でお得なカード</a></li><li><a>家計管理に便利なカード</a></li>
        </ul>
        <div class="mascot" role="img" aria-label="案内役のマスコットキャラクター"></div>
      </div>
    </section>

    <section class="section">
      <h3 class="sub-title orange">カード選定ひろばの新着記事</h3>
      <ul class="news">
        <li><span class="date">2011/08/10</span> <a>ルミナカードの入会特典が更新されました</a></li>
        <li><span class="date">2011/08/05</span> <a>マイル還元率ランキングを更新しました</a></li>
        <li><span class="date">2011/07/28</span> <a>新しい特集記事を公開しました</a></li>
        <li><span class="date">2011/07/20</span> <a>年会費比較データを更新しました</a></li>
        <li><span class="date">2011/07/12</span> <a>ゴールドカード特集を追加しました</a></li>
        <li><span class="date">2011/07/01</span> <a>入会キャンペーン情報を更新しました</a></li>
      </ul>
      <p class="more"><a>新着記事一覧へ ▸</a></p>
    </section>
  </main>

  <aside class="sidebar">
    <div class="side-banner green">クレジットカードを探す</div>
    <div class="side-banner blue">カードの選び方</div>
    <div class="promo">
      <p class="label">ご入会キャンペーン実施中</p>
      <p class="big">最大17,000マイル</p>
      <p class="note">期間限定・当サイト経由のお申込みが対象です</p>
    </div>
    <div class="notice">
      <h3>お知らせ</h3>
      <p>入会キャンペーン情報を毎週更新しています。</p>
    </div>
    <div class="campaigns">
      <h2 class="section-title">おすすめの入会キャンペーン</h2>
      <div class="campaign"><div class="card-art" role="img" aria-label="カード券面" style="background:linear-gradient(#e8eef5,#b9c6d6)"></div><div><h4>ルミナカード</h4><p class="gift">最大8,000円分プレゼント</p><p>新規入会とご利用で特典。</p></div></div>
      <div class="campaign"><div class="card-art" role="img" aria-label="カード券面" style="background:linear-gradient(#dfe9f3,#8fa9c6)"></div><div><h4>アオバカード</h4><p class="gift">最大5,000ポイント</p><p>入会後3か月の利用が対象。</p></div></div>
      <div class="campaign"><div class="card-art" role="img" aria-label="カード券面" style="background:linear-gradient(#eef2f6,#c9d2dc)"></div><div><h4>ソラノ航空カード</h4><p class="gift">最大17,000マイル</p><p>期間中の入会で特典。</p></div></div>
      <div class="campaign"><div class="card-art" role="img" aria-label="カード券面" style="background:linear-gradient(#4a4a4a,#1e1e1e)"></div><div><h4>ミライゴールド</h4><p class="gift">初年度年会費無料</p><p>ゴールド特典付き。</p></div></div>
      <div class="campaign"><div class="card-art" role="img" aria-label="カード券面" style="background:linear-gradient(#f3e3e3,#d4a9a9)"></div><div><h4>ハナカード</h4><p class="gift">最大6,000円分還元</p><p>女性に人気の特典。</p></div></div>
      <div class="campaign"><div class="card-art" role="img" aria-label="カード券面" style="background:linear-gradient(#e6f0e1,#a9c59a)"></div><div><h4>ミドリカード</h4><p class="gift">最大4,000ポイント</p><p>ネット申込限定特典。</p></div></div>
      <div class="campaign"><div class="card-art" role="img" aria-label="カード券面" style="background:linear-gradient(#f5edd8,#d9c18c)"></div><div><h4>コハクカード</h4><p class="gift">最大3,000円分</p><p>入会とご利用が条件。</p></div></div>
    </div>
  </aside>
</div>

<footer class="site-footer">
  <div class="footer-bar">
    <form class="site-search"><span>当サイト内検索</span><input type="text" aria-label="サイト内検索"><button type="button">検索</button></form>
    <div class="social"><span>frendloop いいね!</span><span>Zephrix +1</span><p>気に入ったらボタンを押してください</p></div>
  </div>
  <div class="about">
    <strong>当サイトについて</strong><a>運営会社とお問い合わせ先</a><a>サイトマップ</a><a>プライバシーポリシー</a><a>免責事項</a>
  </div>
  <p class="copyright">Copyright © 2011 カード選定ひろば All Rights Reserved.</p>
</footer>
</body>
</html>
```